Medical Practice Business Card

we need a business card for our new medical ophthalmology practice based in Needham Massachusetts. we are looking for a simple , modern and elegant design.
the card needs to contain the following
1- the logo of our practice (please see attached file)
2- the name of the practice : "Harbor Crest Vision Care"
3- Doctor's Name: Tobias Werrin MD PhD
4- Specialty: Board-Certified Vitreoretinal Surgeon
5- practice address: 382 Palden Ave, Suite 210, Westmere RI 02891
7- Office number: 617- 418 - 2297
8- fax number: 617- 729 - 3186
9- email: info@hcvisioncare.com
10- website: www.hcvisioncare.com
see description

```html
<!DOCTYPE html>
<html lang="en">
<head>
<meta charset="utf-8">
<title>Harbor Crest Vision Care – Business Card</title>
<link href="https://fonts.googleapis.com/css2?family=Montserrat:wght@500;600;700&display=swap" rel="stylesheet">
<style>
  :root {
    --bg: #e3e3e3;
    --paper: #ffffff;
    --navy: #1a3a5e;
    --navy-deep: #18375b;
    --navy-soft: #27486f;
    --sky: #5aa8d6;
    --ink: #4a4a4a;
  }
  html, body {
    margin: 0;
    padding: 0;
    width: 1200px;
    height: 1059px;
    overflow: hidden;
    background: var(--bg);
    font-family: "Montserrat", Arial, sans-serif;
  }
  .canvas { position: relative; width: 1200px; height: 1059px; }

  .card-front {
    position: absolute; left: 256px; top: 100px;
    width: 688px; height: 391px;
    background: var(--paper);
    overflow: hidden;
  }
  .brand {
    position: absolute; right: 36px; top: 46px;
    display: flex; align-items: center; gap: 14px;
  }
  .brand-mark {
    width: 16px; height: 16px; border-radius: 50%;
    border: 3px solid var(--navy);
  }
  .brand-name {
    color: var(--navy);
    font-weight: 600;
    font-size: 24px;
    line-height: 29px;
    text-align: right;
    letter-spacing: 0.5px;
  }
  .doctor-name {
    position: absolute; left: 36px; top: 181px;
    margin: 0;
    color: var(--navy);
    font-weight: 700; font-size: 28px; letter-spacing: 0.5px;
  }
  .specialty {
    position: absolute; left: 38px; top: 216px;
    margin: 0;
    color: var(--ink);
    font-weight: 500; font-size: 18px; letter-spacing: 0.4px;
  }
  .divider {
    position: absolute; left: 36px; right: 36px; top: 250px;
    height: 1px; background: var(--sky);
  }
  .contacts {
    position: absolute; left: 36px; top: 264px;
    margin: 0; padding: 0; list-style: none;
  }
  .contacts li {
    display: flex; align-items: center; gap: 6px;
    height: 28px;
    color: var(--ink); font-weight: 500; font-size: 19px; letter-spacing: 0.3px;
  }
  .contacts svg { width: 16px; height: 16px; fill: var(--sky); }
  .address {
    position: absolute; right: 36px; top: 298px;
    margin: 0; text-align: right;
    color: var(--ink); font-style: normal;
    font-weight: 500; font-size: 18px; line-height: 23px; letter-spacing: 0.4px;
  }
  .web-row {
    position: absolute; left: 0; right: 0; top: 353px;
    display: flex; align-items: center;
  }
  .web-row .rule { height: 2px; background: var(--sky); }
  .web-row .rule-left { flex: 1; }
  .web-row .rule-right { width: 30px; }
  .website {
    padding: 0 4px;
    color: var(--ink); font-weight: 500; font-size: 18px; letter-spacing: 0.4px;
  }
  .website .domain { color: var(--sky); }
  .base-band {
    position: absolute; left: 0; right: 0; bottom: 0;
    height: 11px; background: var(--navy-deep);
  }

  .card-back {
    position: absolute; left: 253px; top: 537px;
    width: 694px; height: 394px;
    background: var(--navy-deep);
    display: flex; align-items: center; justify-content: center;
  }
  .back-brand {
    display: flex; align-items: center; gap: 22px;
  }
  .back-brand .brand-mark {
    width: 26px; height: 26px; border: 4px solid var(--navy-soft);
  }
  .back-brand .brand-name {
    color: var(--navy-soft);
    font-size: 40px; line-height: 50px; text-align: left;
  }
</style>
</head>
<body>
<main class="canvas">
  <section class="card-front" aria-label="Business card front">
    <div class="brand">
      <span class="brand-mark"></span>
      <div class="brand-name">Harbor Crest<br>Vision Care</div>
    </div>

    <h1 class="doctor-name">TOBIAS WERRIN MD PHD</h1>
    <p class="specialty">Board-Certified Vitreoretinal Surgeon</p>
    <div class="divider"></div>

    <ul class="contacts">
      <li>
        <svg viewBox="0 0 24 24" aria-hidden="true"><path d="M6.6 10.8a15.1 15.1 0 0 0 6.6 6.6l2.2-2.2a1 1 0 0 1 1-.25 11.4 11.4 0 0 0 3.6.57 1 1 0 0 1 1 1V20a1 1 0 0 1-1 1A17 17 0 0 1 3 4a1 1 0 0 1 1-1h3.5a1 1 0 0 1 1 1c0 1.25.2 2.45.57 3.57a1 1 0 0 1-.25 1z"/></svg>
        617- 418 - 2297
      </li>
      <li>
        <svg viewBox="0 0 24 24" aria-hidden="true"><path d="M6 2h12v5H6zM3 8h18a2 2 0 0 1 2 2v7h-4v5H5v-5H1v-7a2 2 0 0 1 2-2zm4 8v4h10v-4z"/></svg>
        617- 729 - 3186
      </li>
      <li>
        <svg viewBox="0 0 24 24" aria-hidden="true"><path d="M2 5h20v14H2zm2 2v.5l8 6 8-6V7l-8 6z"/></svg>
        info@hcvisioncare.com
      </li>
    </ul>

    <address class="address">382 Palden Ave, Suite 210<br>Westmere, RI 02891</address>

    <div class="web-row">
      <span class="rule rule-left"></span>
      <span class="website">www.<span class="domain">hcvisioncare</span>.com</span>
      <span class="rule rule-right"></span>
    </div>
    <div class="base-band"></div>
  </section>

  <section class="card-back" aria-label="Business card back">
    <div class="back-brand">
      <span class="brand-mark"></span>
      <div class="brand-name">Harbor Crest<br>Vision Care</div>
    </div>
  </section>
</main>
</body>
</html>
```